Brochure Design Project / IT Consulting Firm

We need a brochure for a IT consulting firm based in Chile.
We are the subsidiary of a french based multinational (www.groupe-vorlen.example).
Our purpose is to solve our customers IT needs, while our vision is to become the premier IT company in Chile.
We delivery basically three types of services:
- software development
- system integration
- consulting
The brochure must be:
- innovative (not the classical boring IT consulting firm with the handshaking stock image in the cover)
- clear and concise designed
Website: http://www.pkmarsa.example
Headquarter website: http://www.groupe-vorlen.example
Chilean recruiting blog: http://sumatebrovel.example
Files added:
- powerpoint file with our corporate presentation (is in Spanish).
- psd and png with our logo
- sample design of a folder we did
Note:
- maybe not all the content of the ppt will be put into the brochure, it should serve as an idea of the content that we should have inside
- we may create different version with different contents of the same brochure, for different services/markets we serve
Target Market(s)
CxO and managers
Industry/Entity Type
Software
Look and feel
Each slider illustrates characteristics of the customer's brand and the style your logo design should communicate.

```html
<!DOCTYPE html>
<html lang="es">
<head>
<meta charset="utf-8">
<title>Pkmarsa Chile – Brochure</title>
<link rel="stylesheet" href="https://fonts.googleapis.com/css2?family=Open+Sans:wght@400;600;700;800&display=swap">
<style>
:root{
  --bg:#3a3a3a;
  --page:#f1f1f1;
  --panel:#e3e3e3;
  --navy:#1f4f82;
  --blue:#2a6bb5;
  --blue-dark:#1c3f7a;
  --orange:#f26a1b;
  --orange-light:#f7a21b;
  --red:#b3162a;
  --red-dark:#8a0e1e;
  --text:#4a4a4a;
  --muted:#7a7a7a;
  --white:#ffffff;
}
*{box-sizing:border-box;margin:0;padding:0}
html,body{width:1200px;height:793px;overflow:hidden}
body{background:var(--bg);font-family:"Open Sans",Arial,sans-serif;color:var(--text);position:relative}
.spread{position:absolute;left:60px;top:40px;width:1080px;height:713px;display:flex;box-shadow:0 8px 30px rgba(0,0,0,.5)}
.page{position:relative;width:540px;height:713px;background:var(--page)}
.page--left{background:linear-gradient(90deg,var(--page) 90%,#dcdcdc)}
.page--right{background:linear-gradient(90deg,#dcdcdc,var(--page) 10%)}
.edge-band{position:absolute;left:0;top:0;bottom:0;width:16px;background:var(--navy)}
.edge-stripe{position:absolute;left:16px;top:0;bottom:0;width:6px;background:var(--orange)}
.brand{position:absolute;left:48px;top:26px;line-height:1}
.brand__name{font-size:30px;font-weight:800;color:var(--navy);letter-spacing:-1px}
.brand__name span{color:var(--orange)}
.brand__country{font-size:9px;font-weight:700;letter-spacing:3px;color:var(--navy);margin-left:52px}
.site-url{position:absolute;right:34px;top:30px;font-size:8px;color:var(--muted)}
.hero-photo{position:absolute;left:46px;top:70px;width:462px;height:352px;background:linear-gradient(160deg,#f4f5f7,#cfd6de 60%,#9aa6b4)}
.box{position:absolute;background:var(--panel);box-shadow:2px 3px 5px rgba(0,0,0,.25)}
.box__head{height:26px;background:linear-gradient(90deg,var(--orange),var(--orange-light));color:var(--white);font-weight:800;font-size:12px;line-height:26px;padding-left:10px;text-transform:uppercase}
.box__body{padding:10px 12px;font-size:7.2px;line-height:1.5}
.about{left:46px;top:436px;width:224px;height:254px}
.sectors{left:284px;top:436px;width:224px;height:254px}
.tag{background:var(--navy);color:var(--white);text-align:center;font-size:7px;padding:2px 0;margin:8px 0 5px}
.center{text-align:center}
.sector-list{list-style:none;margin-top:8px;font-size:8.5px;line-height:1.75;color:var(--muted)}
.sector-list li::before{content:"• "}
.section-bar{position:absolute;left:20px;right:20px;top:22px;height:34px;background:linear-gradient(90deg,var(--orange),var(--orange-light) 60%,var(--orange));color:var(--white);font-weight:800;font-size:17px;text-align:right;padding-right:14px;line-height:34px}
.chart{position:absolute;width:235px;height:160px;background:var(--white);border:1px solid #cfcfcf;box-shadow:2px 3px 5px rgba(0,0,0,.2)}
.chart svg{display:block}
.quality{left:20px;top:420px;width:240px;height:268px}
.badges{display:flex;gap:30px;justify-content:center;margin-top:14px}
.badge{width:64px;height:40px;border-radius:20px;background:#c7c7c7}
.badge--round{width:44px;height:44px;border-radius:50%;background:#b99184}
.clients{left:276px;top:420px;width:244px;height:268px}
.clients__photo{margin:8px 10px 0;height:74px;background:linear-gradient(180deg,#fbfbfb,#d9d2cc)}
.client-grid{display:grid;grid-template-columns:repeat(3,1fr);gap:6px;padding:8px 10px}
.client{background:var(--white);height:20px;display:flex;align-items:center;justify-content:center;font-size:8px;font-weight:700;color:var(--navy);box-shadow:0 1px 2px rgba(0,0,0,.2)}
</style>
</head>
<body>
<div class="spread">
  <section class="page page--left">
    <div class="edge-band"></div>
    <div class="edge-stripe"></div>
    <div class="brand">
      <div class="brand__name">Pk<span>marsa</span></div>
      <div class="brand__country">CHILE</div>
    </div>
    <div class="site-url">www.groupe-vorlen.example</div>
    <div class="hero-photo" role="img" aria-label="Equipo de consultores reunidos alrededor de una mesa de trabajo blanca, vista desde arriba"></div>

    <article class="box about">
      <h2 class="box__head">Quiénes somos</h2>
      <div class="box__body">
        <p>Pkmarsa Chile es un proveedor de servicios de ingeniería multinacional, que presta soluciones de valor añadido y proyectos de tecnología de la información y comunicación a las principales empresas del mundo, y contribuye al desarrollo de las tecnologías más innovadoras y avanzadas.</p>
        <p>Nuestra estrategia de crecimiento es simple: ofrecer los mejores consultores, entregar proyectos de éxito, y hacer que nuestra reputación nos preceda.</p>
        <div class="tag">Groupe Vorlen (desde 1979)</div>
        <p class="center">4.000 ingenieros en 12 países<br>Empresa cotizada en la Bolsa de París desde 1999<br>Ingresos en 2010: 222 M€ · Equity: 53 M€</p>
        <div class="tag">Pkmarsa Chile – Groupe Vorlen (desde 2010)</div>
        <p class="center">85 ingenieros en Santiago<br>Trabajando para 12 grandes clientes<br>Entre las compañías de mayor crecimiento en Chile<br>Ingresos estimados 2011: 1.100 millones de CLP</p>
      </div>
    </article>

    <article class="box sectors">
      <h2 class="box__head">Sectores</h2>
      <div class="box__body">
        <p>Muchas medianas y grandes compañías de diferentes sectores se han depositado su confianza en los servicios ofrecidos por Pkmarsa. Nuestros servicios son flexibles y se adaptan para proporcionar las mejores soluciones para nuestros clientes.</p>
        <ul class="sector-list">
          <li>Banca</li>
          <li>Seguros</li>
          <li>Telecomunicaciones</li>
          <li>Retail &amp; FMCG (fast-moving Consumer Goods)</li>
          <li>Construcción</li>
          <li>Electrónica</li>
          <li>Industria</li>
          <li>Minería</li>
          <li>Transporte y logística</li>
        </ul>
      </div>
    </article>
  </section>

  <section class="page page--right">
    <h1 class="section-bar">CIFRAS CLAVE</h1>

    <figure class="chart" style="left:20px;top:72px">
      <svg width="235" height="160" viewBox="0 0 235 160" font-family="Open Sans, sans-serif">
        <defs>
          <linearGradient id="gBlue" x1="0" y1="0" x2="0" y2="1"><stop offset="0" stop-color="#2a6bb5"/><stop offset="1" stop-color="#1c3f7a"/></linearGradient>
          <linearGradient id="gRed" x1="0" y1="0" x2="0" y2="1"><stop offset="0" stop-color="#c81d33"/><stop offset="1" stop-color="#8a0e1e"/></linearGradient>
        </defs>
        <text x="10" y="20" font-size="8" fill="#666">EMPLEADOS - CHILE</text>
        <rect x="12" y="143" width="50" height="9" fill="url(#gBlue)"/>
        <rect x="75" y="112" width="50" height="40" fill="url(#gBlue)"/>
        <rect x="138" y="55" width="50" height="97" fill="url(#gBlue)"/>
        <polyline points="10,130 70,108 135,58 200,12" fill="none" stroke="#f7a21b" stroke-width="2"/>
        <text x="16" y="140" font-size="6" fill="#333">2010</text>
        <text x="80" y="109" font-size="6" fill="#333">2011</text>
        <text x="143" y="52" font-size="6" fill="#333">2012*</text>
        <text x="100" y="130" font-size="8" fill="#fff" text-anchor="middle">85</text>
        <text x="163" y="75" font-size="8" fill="#fff" text-anchor="middle">189</text>
      </svg>
    </figure>

    <figure class="chart" style="left:282px;top:72px">
      <svg width="235" height="160" viewBox="0 0 235 160" font-family="Open Sans, sans-serif">
        <text x="10" y="20" font-size="8" fill="#666">INGRESOS - CHILE</text>
        <rect x="12" y="34" width="7" height="7" fill="#b3162a"/>
        <text x="23" y="40" font-size="6" fill="#666">millones de Pesos</text>
        <rect x="12" y="144" width="50" height="8" fill="url(#gRed)"/>
        <rect x="75" y="124" width="50" height="28" fill="url(#gRed)"/>
        <rect x="138" y="48" width="50" height="104" fill="url(#gRed)"/>
        <polyline points="10,138 70,120 135,52 200,14" fill="none" stroke="#f7a21b" stroke-width="2"/>
        <text x="16" y="141" font-size="6" fill="#333">2010</text>
        <text x="80" y="121" font-size="6" fill="#333">2011</text>
        <text x="143" y="45" font-size="6" fill="#333">2012*</text>
        <text x="100" y="142" font-size="8" fill="#fff" text-anchor="middle">1100</text>
        <text x="163" y="72" font-size="8" fill="#fff" text-anchor="middle">3200</text>
      </svg>
    </figure>

    <figure class="chart" style="left:20px;top:246px">
      <svg width="235" height="160" viewBox="0 0 235 160" font-family="Open Sans, sans-serif">
        <text x="10" y="20" font-size="8" fill="#666">EMPLEADOS - CHILE</text>
        <rect x="12" y="106" width="34" height="46" fill="url(#gBlue)"/>
        <rect x="52" y="100" width="34" height="52" fill="url(#gBlue)"/>
        <rect x="92" y="78" width="34" height="74" fill="url(#gBlue)"/>
        <rect x="132" y="72" width="34" height="80" fill="url(#gBlue)"/>
        <rect x="172" y="52" width="34" height="100" fill="url(#gBlue)"/>
        <polyline points="8,108 50,96 90,74 130,66 172,48 212,14" fill="none" stroke="#f7a21b" stroke-width="2"/>
        <text x="16" y="103" font-size="6" fill="#333">2007</text>
        <text x="56" y="97" font-size="6" fill="#333">2008</text>
        <text x="96" y="75" font-size="6" fill="#333">2009</text>
        <text x="136" y="69" font-size="6" fill="#333">2010</text>
        <text x="176" y="49" font-size="6" fill="#333">2011</text>
        <text x="29" y="138" font-size="7" fill="#fff" text-anchor="middle">1900</text>
        <text x="69" y="132" font-size="7" fill="#fff" text-anchor="middle">2100</text>
        <text x="109" y="112" font-size="7" fill="#fff" text-anchor="middle">3000</text>
        <text x="149" y="106" font-size="7" fill="#fff" text-anchor="middle">3200</text>
        <text x="189" y="80" font-size="7" fill="#fff" text-anchor="middle">4000</text>
      </svg>
    </figure>

    <figure class="chart" style="left:282px;top:246px">
      <svg width="235" height="160" viewBox="0 0 235 160" font-family="Open Sans, sans-serif">
        <text x="10" y="20" font-size="8" fill="#666">INGRESOS - CHILE</text>
        <rect x="12" y="34" width="7" height="7" fill="#b3162a"/>
        <text x="23" y="40" font-size="6" fill="#666">millones de Euros</text>
        <rect x="12" y="124" width="40" height="28" fill="url(#gRed)"/>
        <rect x="60" y="104" width="40" height="48" fill="url(#gRed)"/>
        <rect x="108" y="88" width="40" height="64" fill="url(#gRed)"/>
        <rect x="156" y="52" width="40" height="100" fill="url(#gRed)"/>
        <polyline points="8,120 58,100 106,84 154,48 210,12" fill="none" stroke="#f7a21b" stroke-width="2"/>
        <text x="14" y="121" font-size="5.5" fill="#333">2007/08</text>
        <text x="62" y="101" font-size="5.5" fill="#333">2008/09</text>
        <text x="108" y="85" font-size="5.5" fill="#333">2009/2010</text>
        <text x="156" y="49" font-size="5.5" fill="#333">2010/2011</text>
        <text x="32" y="142" font-size="7" fill="#fff" text-anchor="middle">149</text>
        <text x="80" y="132" font-size="7" fill="#fff" text-anchor="middle">175</text>
        <text x="128" y="124" font-size="7" fill="#fff" text-anchor="middle">190</text>
        <text x="176" y="84" font-size="7" fill="#fff" text-anchor="middle">222</text>
      </svg>
    </figure>

    <article class="box quality">
      <h2 class="box__head">Calidad</h2>
      <div class="box__body">
        <p>Para asegurar la excelencia de los servicios que prestamos de acuerdo a los resultados comprometidos, Pkmarsa utiliza las mejores estándares disponibles en el mercado de las buenas prácticas en el área de ingeniería de software (metodologías ágiles e iterativas), gestión de proyectos, gestión de servicios de TI, aumento de la eficacia de la organización y la gestión integral de la calidad a través de la norma ISO 9001:2008.</p>
        <p>Comprometidos con la calidad globalmente desde 1992, nuestro departamento de Quality Assurance vela por el cumplimiento de nuestra Política de Calidad y por garantizar los acuerdos de niveles de servicio de nuestros proyectos.</p>
        <div class="badges">
          <div class="badge" role="img" aria-label="Sello de certificación de madurez de procesos"></div>
          <div class="badge badge--round" role="img" aria-label="Sello de buenas prácticas de servicios TI"></div>
        </div>
      </div>
    </article>

    <article class="box clients">
      <h2 class="box__head">Algunos clientes</h2>
      <div class="clients__photo" role="img" aria-label="Hilera de pequeñas casas de colores sobre fondo claro"></div>
      <div class="client-grid">
        <div class="client">Norvia</div>
        <div class="client">Altamar</div>
        <div class="client">Pelcro Vida</div>
        <div class="client">Tenvar</div>
        <div class="client">Qrino</div>
        <div class="client">Lumbra</div>
        <div class="client">Datalis</div>
        <div class="client">Osvent</div>
        <div class="client">Ferrina</div>
        <div class="client">Brenca</div>
        <div class="client">Halvo</div>
      </div>
    </article>
  </section>
</div>
</body>
</html>
```